Business Card & Stationary Design Project

We are looking for some creative direction for business cards and our stationary.

We are a global logistics firm that has recently changed its name to Marwick Global Logistics and we have a new website due out tomorrow (www.marwick.com.au).

The colours of the company are rich navy tones, I would like to have business cards that fit together to make one picture on the back (possibly an old map of the world??), and the front to be modern contemporary looking.

But I am open to suggestions, so just incorporate our new logo and get going!
Updates

Hi Everyone,

Thank you for all of your designs so far and the time you have put into it.

I have asked many of you for amendments to see if we can get a final product, so with this in mind I am extending the deadline by a few days.

Good luck and thank you once again.

Please message me direct if you need any clarification.

Kind Regards
Tobias

Reason: As outlined the extra 3 days is for amendments and changes to the current submissions. Thanks Tobias

Industry/Entity Type

Business

```html
<!DOCTYPE html>
<html lang="en">
<head>
<meta charset="utf-8">
<title>Marwick Global Logistics – Business Card</title>
<link rel="stylesheet" href="https://fonts.googleapis.com/css2?family=Mulish:wght@400;700&display=swap">
<style>
  :root {
    --backdrop: #2d2e30;
    --paper: #eceae6;
    --navy: #163f78;
    --navy-deep: #0f2f5e;
    --sky: #3a86d0;
    --sky-soft: #5b9fe0;
    --back-top: #1f5aa2;
    --back-bottom: #2f7fca;
    --white: #ffffff;
  }
  * { box-sizing: border-box; margin: 0; padding: 0; }
  html, body {
    width: 1200px; height: 900px; overflow: hidden;
    background: var(--backdrop);
    font-family: "Mulish", sans-serif;
  }
  .stage {
    width: 1200px; height: 900px;
    display: flex; flex-direction: column; align-items: center; justify-content: center;
    gap: 40px;
  }
  .card {
    position: relative;
    width: 680px; height: 389px;
    overflow: hidden;
    box-shadow: 0 10px 26px rgba(0,0,0,.45);
  }

  /* ---------- logo lock-up ---------- */
  .brand {
    position: absolute;
    display: flex; align-items: center; gap: 22px;
  }
  .brand-name {
    color: var(--navy);
    font-weight: 400;
    text-transform: uppercase;
    line-height: 1;
  }
  .brand-name .word { display: block; font-size: 58px; letter-spacing: 18px; }
  .brand-name .line { display: block; font-size: 19px; letter-spacing: 14.5px; margin-top: 10px; }
  .brand-dot {
    width: 56px; height: 56px; border-radius: 50%;
    background: var(--sky);
    flex: none;
  }

  /* ---------- front ---------- */
  .card-front { background: var(--paper); }
  .card-front .brand { left: 70px; top: 46px; }
  .holder { position: absolute; left: 48px; top: 178px; }
  .holder-name { color: var(--navy-deep); font-weight: 700; font-size: 19px; letter-spacing: .3px; }
  .holder-role { color: var(--sky); font-size: 15px; margin-top: 2px; }

  .contact-band {
    position: absolute; left: 0; right: 0; bottom: 0; height: 150px;
    background: var(--navy);
    border-top: 7px solid var(--sky);
  }
  .band-map {
    position: absolute; right: 0; top: 0; width: 300px; height: 100%;
    background: linear-gradient(90deg, rgba(58,134,208,0), rgba(58,134,208,.28));
  }
  .contact {
    position: absolute; color: var(--white); font-size: 15px; line-height: 1.6;
  }
  .contact-row { display: flex; align-items: center; gap: 9px; }
  .icon { width: 15px; height: 15px; flex: none; }
  .contact-phones { left: 48px; top: 20px; }
  .contact-details { left: 250px; top: 20px; }
  .contact-details .address { margin-bottom: 4px; }

  /* ---------- back ---------- */
  .card-back {
    background: linear-gradient(160deg, var(--back-top), var(--back-bottom));
  }
  .back-map {
    position: absolute; left: 90px; right: 40px; top: 160px; bottom: 30px;
    border-radius: 40% 50% 30% 45%;
    background: radial-gradient(ellipse at 50% 50%, rgba(120,180,240,.35), rgba(120,180,240,0) 70%);
  }
  .card-back .brand { left: 96px; top: 118px; }
  .card-back .brand-name { color: var(--white); }
  .card-back .brand-dot { background: var(--sky-soft); }
</style>
</head>
<body>
<main class="stage">

  <!-- front -->
  <section class="card card-front">
    <div class="brand">
      <div class="brand-name"><span class="word">Marwick</span><span class="line">Global Logistics</span></div>
      <span class="brand-dot"></span>
    </div>

    <div class="holder">
      <div class="holder-name">TOBIAS ASHCOMBE</div>
      <div class="holder-role">General Manager</div>
    </div>

    <div class="contact-band">
      <div class="band-map" role="img" aria-label="Faint dotted world map"></div>

      <div class="contact contact-phones">
        <div class="contact-row">
          <svg class="icon" viewBox="0 0 16 16"><circle cx="8" cy="8" r="7.5" fill="none" stroke="#fff" stroke-width="1"/><path d="M5.6 4.2l1.3 1.6-.8 1c.6 1.2 1.4 2 2.6 2.6l1-.8 1.6 1.3-.9 1.3c-2.8-.5-5.2-2.9-5.7-5.7z" fill="#fff"/></svg>
          <span>02 8461 2300</span>
        </div>
        <div class="contact-row">
          <svg class="icon" viewBox="0 0 16 16"><circle cx="8" cy="8" r="7.5" fill="none" stroke="#fff" stroke-width="1"/><rect x="4.5" y="6" width="7" height="5" rx=".8" fill="#fff"/><rect x="5.5" y="4" width="5" height="2.5" fill="#fff"/></svg>
          <span>02 9472 6180</span>
        </div>
      </div>

      <div class="contact contact-details">
        <div class="address">58 Harbour Lane, Pyrmont<br>NSW 2009</div>
        <div class="contact-row">
          <svg class="icon" viewBox="0 0 16 16"><circle cx="8" cy="8" r="7.5" fill="none" stroke="#fff" stroke-width="1"/><rect x="4" y="5" width="8" height="6" fill="none" stroke="#fff" stroke-width="1"/><path d="M4 5l4 3.4L12 5" fill="none" stroke="#fff" stroke-width="1"/></svg>
          <span>tobias@marwick.com.au</span>
        </div>
        <div class="contact-row">
          <svg class="icon" viewBox="0 0 16 16"><circle cx="8" cy="8" r="7" fill="none" stroke="#fff" stroke-width="1"/><ellipse cx="8" cy="8" rx="3" ry="7" fill="none" stroke="#fff" stroke-width="1"/><path d="M1 8h14" stroke="#fff" stroke-width="1"/></svg>
          <span>www.marwick.com.au</span>
        </div>
      </div>
    </div>
  </section>

  <!-- back -->
  <section class="card card-back">
    <div class="back-map" role="img" aria-label="Dotted world map spanning the card back"></div>
    <div class="brand">
      <div class="brand-name"><span class="word">Marwick</span><span class="line">Global Logistics</span></div>
      <span class="brand-dot"></span>
    </div>
  </section>

</main>
</body>
</html>
```